Pell Hartwick - Magazine

Our client would like a magazine designed for a conceptual novelty based on unconventional views on contemporary issues, including; finance, religion, politics etc.!

The novelty includes 1 main article, supporting images and 12 short poems.
We would like the designer to create page vectors, borders, fonts and other layout design elements.

In the first stage of the competition we request:

Magazine layout - 6 pages( 4 article variations based on article content and 2 poem page designs)

We would like to see high impact, striking vectors and design concepts to compliment the article content. See attached bullet point guide to article to help design page themes.

COMPANY INFO
Writer, poet, researcher and commentator. Our client is interested in sharing art and issues he believes in. Our client would like to design one magazine issue first but has a collection of material to produce a series of magazines in the future. So he is looking to establish a potentially long-term partnership with designer(s).

Target Market(s)

Quick and easy to read, coffee time magazine. Target Market: Male 40yrs+, Intellectual, Open Minded.

Industry/Entity Type

Finance

Font styles to use
Serif
Decorative

Requirements
Must have
• Main Article and Poetry: Space for 1 -2 images per page.
A subtle design feature that connects each page.
Primary colors: Jade Green and some Grayscale.
Secondary Colors: 3rd and 4th color open to designers preference.
Page Dimensions : 7.5in height, 7in width.
Articles: Same color theme, different layout and vector choice, same font color and size.
Poetry: Some design creative freedom. Focus on creating a unique title font incorporating the theme of the poem, Poetry TITLE font must be made a feature design element (poem identity)
Font: See Veldtrove Quarterly magazine styling
Columns: Single or multiple.
All vectors and images should be sourced from pixel quarry.
Nice to have
• Images/pictures that connect with article topic and align with color theme.
Should not have
• Avoid repetition of page design. To do this follow the idea of each paragraph (see attached breakdown)

```html
<!DOCTYPE html>
<html lang="en">
<head>
<meta charset="utf-8">
<title>Point Me at the Wry — Pell Hartwick</title>
<link rel="stylesheet" href="https://fonts.googleapis.com/css2?family=Alegreya:ital,wght@0,400;0,700;1,400&family=Zilla+Slab:wght@300;400&family=Montserrat:wght@400&display=swap">
<style>
  :root {
    --jade: #14a89a;
    --ink: #2b2b2b;
    --grey: #9a9a9a;
    --rule: #bdbdbd;
    --paper: #ffffff;
    --backdrop: #f1f1f1;
  }
  * { box-sizing: border-box; margin: 0; padding: 0; }
  html, body { width: 1200px; height: 778px; overflow: hidden; }
  body { background: var(--backdrop); position: relative; font-family: "Alegreya", Georgia, serif; color: var(--ink); }

  .spread { position: absolute; left: 68px; top: 100px; width: 1062px; height: 570px; background: var(--paper); overflow: hidden; }
  .fold { position: absolute; left: 530px; top: 0; width: 1px; height: 100%; background: #d8d8d8; z-index: 3; }

  .abs { position: absolute; z-index: 2; }
  .photo { position: absolute; z-index: 0; }

  .running-rule { position: absolute; top: 30px; height: 0; border-top: 1px dotted var(--rule); z-index: 1; }
  .masthead {
    position: absolute; left: 30px; top: 20px; height: 20px; width: 116px; z-index: 2;
    border-left: 1px solid var(--rule); border-right: 1px solid var(--rule);
    font-family: "Montserrat", Arial, sans-serif; font-size: 7px; letter-spacing: 2.4px;
    color: var(--grey); text-transform: lowercase; display: flex; align-items: center; justify-content: center;
    background: var(--paper);
  }

  .title {
    left: 30px; top: 62px; font-family: "Zilla Slab", Georgia, serif; font-weight: 300;
    font-size: 43px; line-height: 52px; color: var(--jade); letter-spacing: -0.5px; white-space: nowrap;
  }
  .credit-rule { left: 0; top: 124px; width: 30px; border-top: 1px dotted var(--rule); }
  .credit { left: 33px; top: 119px; font-family: "Montserrat", Arial, sans-serif; font-size: 5.5px; color: #777; white-space: nowrap; }

  .column p {
    font-style: italic; font-size: 8.6px; line-height: 13.7px; margin-bottom: 14px;
  }
  .column .deck {
    font-style: normal; font-weight: 700; color: var(--jade);
    font-size: 10.6px; line-height: 13.8px; margin-bottom: 16px;
  }

  .end-mark { display: inline-block; width: 6px; height: 6px; border-radius: 50%; background: var(--jade); vertical-align: middle; margin-left: 2px; }

  .folio-rule { position: absolute; top: 540px; border-top: 1px dotted var(--rule); z-index: 1; }
  .folio {
    position: absolute; top: 533px; width: 14px; height: 14px; border-radius: 50%; z-index: 2;
    background: #cfcfcf; color: #fff; font-family: "Montserrat", Arial, sans-serif;
    font-size: 6px; display: flex; align-items: center; justify-content: center;
  }
</style>
</head>
<body>
<main class="spread">
  <div class="fold"></div>

  <div class="running-rule" style="left:30px; width:495px;"></div>
  <div class="masthead">pell hartwick</div>
  <div class="running-rule" style="left:532px; width:500px;"></div>

  <h1 class="abs title">Point Me at the Wry</h1>
  <div class="abs credit-rule"></div>
  <div class="abs credit">Author XXXXXXXXXXX · Photography XXXXXXXX</div>

  <!-- Left page photography -->
  <div class="photo" role="img" aria-label="Glass medicine vial and syringe with reflection"
       style="left:330px; top:118px; width:200px; height:150px; background:radial-gradient(ellipse at 65% 45%, #dfe4e6 0%, #f3f5f6 45%, #ffffff 75%);"></div>
  <div class="photo" role="img" aria-label="Amber pill bottle, glass vials, ampoules, syringe and capsules"
       style="left:52px; top:360px; width:300px; height:210px; background:radial-gradient(ellipse at 35% 65%, #c8a07a 0%, #e4d3c2 30%, #f4f2f0 58%, #ffffff 80%);"></div>

  <!-- Left page text -->
  <div class="abs column" style="left:31px; top:164px; width:122px;">
    <p>Novam hanc restituen di kalendarii rationem, exiguo volumine compre hensam, ad chris tianos principes ceannos misi mus, ut res quae.</p>
    <p>Novam hanc restituen di kalendarii rationem, exiguo volumine compre lebrioresque universitates pauante annos misi mus, ut res quae.</p>
    <p>Novam hanc restituen di kalendarii rationem, exiguo volumine compre lebrioresque universitates paante annos misi mus, ut res quae.</p>
  </div>
  <div class="abs column" style="left:180px; top:161px; width:128px;">
    <p class="deck">Novam hanc restituen di kalendarii rationem, exiguo celebrioresque universitates pauante annos misi mus, ut res quae.</p>
    <p>Novam hanc restituen di kalendarii rationem, exiguo volumine compre hensam, ad chris tianos principes celebrioresque universitates paante annos misi mus, ut res quae.</p>
  </div>
  <div class="abs column" style="left:365px; top:288px; width:128px;">
    <p>Novam hanc restituen di kalendarii rationem, exiguo volumine compre hensam, ad chris tianos principes celebrioresque universitates pauante annos misi mus, ut res quae.</p>
    <p>Novam hanc restituen di kalendarii rationem, exiguo volumine compre hensam, ad chris tianos principes celebrioresque universitates pauante annos misi mus, ut res quae.</p>
    <p>Novam hanc restituen di kalendarii rationem, exiguo volumine compre hensam, ad chris tianos principes celebrioresque universitates paante annos misi mus, ut res quae.</p>
  </div>

  <!-- Right page photography -->
  <div class="photo" role="img" aria-label="Spilled amber pill bottle with pink, yellow and white capsules"
       style="left:537px; top:232px; width:275px; height:165px; background:radial-gradient(ellipse at 40% 55%, #e9c27e 0%, #f1d6d6 30%, #f7f3ee 58%, #ffffff 80%);"></div>
  <div class="photo" role="img" aria-label="Single golden softgel capsule"
       style="left:897px; top:125px; width:140px; height:100px; background:radial-gradient(ellipse at 50% 45%, #edd58a 0%, #f5e9c6 35%, #ffffff 72%);"></div>
  <div class="photo" role="img" aria-label="Navy blue stethoscope lying flat"
       style="left:532px; top:405px; width:345px; height:162px; background:radial-gradient(ellipse at 45% 50%, #9fb2c6 0%, #dde4eb 40%, #ffffff 78%);"></div>

  <!-- Right page text -->
  <div class="abs column" style="left:600px; top:107px; width:130px;">
    <p class="deck">Novam hanc restituen di kalendarii rationem, exiguo volumine compre hensam, ad chris tianos principes celebrioresque universitates pauante annos misi mus, ut res quae.</p>
  </div>
  <div class="abs column" style="left:756px; top:76px; width:128px;">
    <p>Novam hanc restituen di kalendarii rationem, exiguo volumine compre hensam, ad chris tianos principes celebrioresque universitates pauante annos misi mus, ut res quae.</p>
    <p>Novam hanc restituen di kalendarii rationem, exiguo volumine compre hensam, ad chris tianos principes celebrioresque universitates pauante annos misi mus, ut res quae.</p>
    <p>Novam hanc restituen di kalendarii rationem, exiguo volumine compre hensam, ad chris tianos principes celebrioresque universitates paante annos misi mus, ut res quae.</p>
  </div>
  <div class="abs column" style="left:902px; top:248px; width:128px;">
    <p>Novam hanc restituen di kalendarii rationem, exiguo volumine compre hensam, ad chris tianos principes celebrioresque universitates pauante annos misi mus, ut res quae.</p>
    <p>Novam hanc restituen di kalendarii rationem, exiguo volumine compre hensam, ad chris tianos principes celebrioresque universitates pauante annos misi mus, ut res quae.</p>
    <p>Novam hanc restituen di kalendarii rationem, exiguo volumine compre hensam, ad chris tianos principes celebrioresque universitates paante annos misi mus, ut res quae.<span class="end-mark"></span></p>
  </div>

  <!-- Folios -->
  <div class="folio-rule" style="left:38px; width:490px;"></div>
  <div class="folio" style="left:23px;">8</div>
  <div class="folio-rule" style="left:532px; width:490px;"></div>
  <div class="folio" style="left:1025px;">9</div>
</main>
</body>
</html>
```